Ridgeway Coverage Partners
Business Card, Stationary, Folder jacket, Envelope
Project: Ridgeway Coverage Partners
Ridgeway Coverage Partners -
Creative Brief
Simple
Roy Fenwick
Insurance Professional
24517 Marrow Ave, Suite 400 Dunmere, UT 84921
SLC: 801-555-0143
Direct: 801-555-0178
Roy@RCPquarry.example
www.RCPquarry.example
Utah License No. 718260
We will need a space for a photo to be placed. Also, we will need the ability to customize the card for our different employees as needed. All personal info needs to be editable.
Open to ideas but we may want to have logos for the different insurance companies that we sell for. Examples: The Brellmont, Quorvia auto and home, Pennowick Insurance, Dralle, Tovrin, Ashbrook, TRVL, Wendiver, Pollick, Brisco, Fennimore Casualty, Vale Drivers...

```html
<!DOCTYPE html>
<html lang="en">
<head>
<meta charset="utf-8">
<title>Ridgeway Coverage Partners — Stationery Set</title>
<link rel="stylesheet" href="https://fonts.googleapis.com/css2?family=Cinzel:wght@600&family=Open+Sans:wght@400;600&display=swap">
<style>
  :root {
    --backdrop: #e4e4e4;
    --paper: #fbfbfb;
    --paper-shade: #ececec;
    --brand: #7a1d2b;
    --ink: #3a3a3a;
    --ink-soft: #8a8a8a;
    --rule: #c9c9c9;
    --photo: #cfd3d6;
  }
  * { box-sizing: border-box; margin: 0; padding: 0; }
  html, body { width: 1200px; height: 389px; overflow: hidden; }
  body {
    background: var(--backdrop);
    font-family: "Open Sans", Arial, sans-serif;
    color: var(--ink);
    position: relative;
  }
  .piece {
    position: absolute;
    background: var(--paper);
    box-shadow: 0 2px 6px rgba(0,0,0,.18);
  }
  .wordmark {
    font-family: "Cinzel", Georgia, serif;
    font-weight: 600;
    color: var(--brand);
    line-height: 1.05;
    display: flex;
    align-items: center;
    gap: 4px;
  }
  .wordmark .dot { width: 7px; height: 7px; border-radius: 50%; background: var(--brand); flex: none; }
  .brand-band { position: absolute; left: 0; right: 0; bottom: 0; height: 4px; background: var(--brand); }

  /* business cards */
  .card { width: 104px; height: 62px; }
  .card-front { left: 32px; top: 24px; padding: 8px; }
  .card-front .wordmark { font-size: 7px; }
  .card-front .person { position: absolute; left: 8px; bottom: 10px; font-size: 4.5px; line-height: 1.35; }
  .card-front .person strong { font-size: 6px; color: var(--brand); font-weight: 600; display: block; }
  .card-photo { position: absolute; right: 8px; top: 8px; width: 26px; height: 34px; background: var(--photo); }
  .card-back { left: 32px; top: 140px; padding: 8px; }
  .card-back .wordmark { font-size: 7px; }
  .card-back .person { position: absolute; left: 8px; bottom: 10px; font-size: 4.5px; line-height: 1.35; }
  .card-carriers { left: 32px; top: 236px; padding: 6px; }
  .carrier-grid { display: grid; grid-template-columns: repeat(3, 1fr); gap: 2px 3px; font-size: 4px; color: var(--ink-soft); }
  .carrier-grid span { white-space: nowrap; overflow: hidden; }

  /* envelope and note card */
  .envelope { left: 146px; top: 108px; width: 104px; height: 82px; padding: 8px; }
  .envelope .wordmark { font-size: 6px; }
  .envelope .return { font-size: 3.5px; color: var(--ink-soft); margin-top: 3px; }
  .note-card { left: 248px; top: 230px; width: 38px; height: 54px; padding: 5px; }
  .note-card .wordmark { font-size: 4px; }
  .note-lines { margin-top: 8px; }
  .note-lines i { display: block; height: 1px; background: var(--rule); margin-bottom: 5px; }

  /* letterhead */
  .letterhead { left: 318px; top: 36px; width: 196px; height: 336px; padding: 14px; }
  .letterhead .wordmark { font-size: 11px; }
  .letterhead .footer { position: absolute; left: 14px; right: 14px; bottom: 10px; font-size: 4.5px; color: var(--ink-soft); text-align: center; }

  /* fax cover */
  .fax { left: 536px; top: 58px; width: 164px; height: 312px; padding: 12px; }
  .fax .wordmark { font-size: 9px; }
  .fax-title { position: absolute; right: 14px; top: 44px; font-size: 14px; font-weight: 600; }
  .fax-fields { margin-top: 40px; display: grid; grid-template-columns: 1fr 1fr; gap: 6px 8px; font-size: 5px; }
  .fax-fields span { border-bottom: 1px solid var(--rule); padding-bottom: 2px; }
  .fax-checks { display: flex; gap: 6px; margin-top: 10px; font-size: 4.5px; }
  .fax-checks span::before { content: ""; display: inline-block; width: 4px; height: 4px; border: 1px solid var(--ink); margin-right: 2px; vertical-align: -1px; }
  .fax-notes { position: absolute; left: 12px; right: 12px; top: 140px; bottom: 30px; border: 1px solid var(--rule); }
  .fax .footer { position: absolute; left: 12px; right: 12px; bottom: 10px; font-size: 4.5px; color: var(--ink-soft); text-align: center; }

  /* folder */
  .folder-front { left: 768px; top: 48px; width: 196px; height: 270px; }
  .folder-front .wordmark { position: absolute; right: 16px; top: 110px; font-size: 11px; }
  .folder-front .footer { position: absolute; left: 0; right: 0; bottom: 12px; font-size: 4.5px; color: var(--ink-soft); text-align: center; }
  .folder-open { left: 988px; top: 48px; width: 180px; height: 270px; background: var(--paper-shade); }
  .folder-pocket { position: absolute; left: 0; right: 0; bottom: 0; height: 120px; }
  .folder-pocket .wordmark { position: absolute; left: 14px; top: 40px; font-size: 8px; }
</style>
</head>
<body>

  <section class="piece card card-front" aria-label="Business card front">
    <div class="wordmark"><span class="dot"></span>Ridgeway Coverage Partners</div>
    <div class="card-photo" role="img" aria-label="Space for employee photo"></div>
    <div class="person">
      <strong>Roy Fenwick</strong>
      Insurance Professional<br>
      SLC: 801-555-0143 · Direct: 801-555-0178<br>
      Roy@RCPquarry.example
    </div>
    <div class="brand-band"></div>
  </section>

  <section class="piece card card-back" aria-label="Business card reverse">
    <div class="wordmark"><span class="dot"></span>Ridgeway Coverage Partners</div>
    <div class="person">
      24517 Marrow Ave, Suite 400 Dunmere, UT 84921<br>
      www.RCPquarry.example<br>
      Utah License No. 718260
    </div>
    <div class="brand-band"></div>
  </section>

  <section class="piece card card-carriers" aria-label="Carrier card">
    <div class="carrier-grid">
      <span>The Brellmont</span><span>Quorvia</span><span>Pennowick Insurance</span>
      <span>Dralle</span><span>Tovrin</span><span>Ashbrook</span>
      <span>TRVL</span><span>Wendiver</span><span>Pollick</span>
      <span>Brisco</span><span>Fennimore Casualty</span><span>Vale Drivers</span>
    </div>
  </section>

  <section class="piece envelope" aria-label="Envelope">
    <div class="wordmark"><span class="dot"></span>Ridgeway Coverage Partners</div>
    <div class="return">24517 Marrow Ave, Suite 400 Dunmere, UT 84921</div>
    <div class="brand-band"></div>
  </section>

  <section class="piece note-card" aria-label="Note card">
    <div class="wordmark">RCP</div>
    <div class="note-lines"><i></i><i></i><i></i><i></i></div>
  </section>

  <section class="piece letterhead" aria-label="Letterhead">
    <div class="wordmark"><span class="dot"></span>Ridgeway Coverage<br>Partners</div>
    <div class="footer">24517 Marrow Ave, Suite 400 Dunmere, UT 84921 · 801-555-0143 · www.RCPquarry.example</div>
    <div class="brand-band"></div>
  </section>

  <section class="piece fax" aria-label="Fax cover sheet">
    <div class="wordmark"><span class="dot"></span>Ridgeway Coverage<br>Partners</div>
    <div class="fax-title">Fax</div>
    <div class="fax-fields">
      <span>To:</span><span>From:</span>
      <span>Fax:</span><span>Pages:</span>
      <span>Phone:</span><span>Date:</span>
      <span>Re:</span><span>CC:</span>
    </div>
    <div class="fax-checks">
      <span>Urgent</span><span>Review</span><span>Comment</span><span>Reply</span><span>Recycle</span>
    </div>
    <div class="fax-notes"></div>
    <div class="footer">24517 Marrow Ave, Suite 400 Dunmere, UT 84921 · 801-555-0143</div>
  </section>

  <section class="piece folder-front" aria-label="Presentation folder cover">
    <div class="wordmark"><span class="dot"></span>Ridgeway Coverage<br>Partners</div>
    <div class="footer">www.RCPquarry.example · 801-555-0143</div>
    <div class="brand-band"></div>
  </section>

  <section class="piece folder-open" aria-label="Presentation folder inside pocket">
    <div class="piece folder-pocket">
      <svg width="180" height="14" style="position:absolute;top:0;left:0" aria-hidden="true">
        <path d="M0 0 Q90 14 180 0" fill="none" stroke="var(--rule)" stroke-width="1"/>
      </svg>
      <div class="wordmark"><span class="dot"></span>Ridgeway Coverage Partners</div>
      <div class="brand-band"></div>
    </div>
  </section>

</body>
</html>
```